依頼詳細
ラベルのデザインを募集します。

基本的には、幅91.5mm 縦131mmの縦長で角が少し丸いシールにいれるデザインです
・データは様々な形で使用させて頂きます。
(ホームページに載せたり、サンプル品に使用するなど)

クラフトのチャック袋(スタンドパック)にラベルを貼る予定です。
■キャッチフレーズなど
・魔法のスーパーフード タイガーナッツ!パウダータイプ

記載項目
商品名:星屑のコモレビパウダー
その他キャッチフレーズ、キーワードなど:スーパーフード
希望イメージ
シンプル 複雑
単色 カラフル
暗い 明るい
日常 高級
遊び心 厳粛
未来的 伝統的
女性的 男性的
希望する色
赤系、黄・オレンジ系
納品ファイル
• イラストレーター形式 (.ai)
• フォトショップ形式 (.psd)
補足説明
送付ファイルはパウダーの写真です。特に使わなくても大丈夫ですが、色合いなど確認するのにお使いください。
粒状態の画像を追加します。
製品自体は粉なので参考にしてください。
使わなくても大丈夫です。
■ 選んだ理由

自分の考えていたイメージに近く、魔法感がよく出ていて
まとまっていたのでこちらを選ばせて頂きました。

■ 提案者全員のお礼・コメント

多数のご応募ありがとうございました。
またの機会がありましたら、よろしくお願い足します。

```html
<!DOCTYPE html>
<html lang="ja">
<head>
<meta charset="utf-8">
<title>星屑のコモレビパウダー ラベル</title>
<link rel="stylesheet" href="https://fonts.googleapis.com/css2?family=Lato:wght@700&family=Playfair+Display:wght@500&family=M+PLUS+1p:wght@800&family=Noto+Sans+JP:wght@500&display=swap">
<style>
  :root {
    --paper: #ffffff;
    --edge: #b9b9b9;
    --amber: #c8701a;
    --wine: #8a1a1a;
    --red-hi: #e8342a;
    --red-lo: #a50f12;
    --gold: #f2c14e;
    --gold-deep: #c98a1d;
    --sun: #f7a81b;
    --sun-soft: #ffd65a;
    --ink: #2b2b2b;
  }
  * { margin: 0; padding: 0; box-sizing: border-box; }
  html, body { width: 893px; height: 1200px; overflow: hidden; background: var(--paper); }
  .label {
    position: relative;
    width: 893px; height: 1200px;
    background: var(--paper);
  }
  .label-edge {
    position: absolute; left: 24px; top: 24px; right: 24px; bottom: 24px;
    border: 3px solid var(--edge); border-radius: 42px;
  }
  .tagline {
    position: absolute; top: 52px; width: 100%; text-align: center;
    font-family: "Lato", sans-serif; font-weight: 700; font-size: 30px;
    letter-spacing: 2px; color: var(--amber);
  }
  .english-name {
    position: absolute; top: 98px; width: 100%; text-align: center;
    font-family: "Playfair Display", serif; font-weight: 500; font-size: 46px;
    color: var(--wine);
  }
  .art { position: absolute; left: 0; top: 0; }
  .product-name {
    position: absolute; left: 160px; top: 240px; width: 573px; text-align: center;
    font-family: "M PLUS 1p", sans-serif; font-weight: 800; font-size: 74px; line-height: 82px;
    color: #fff; text-shadow: 0 3px 0 rgba(110, 0, 0, 0.55);
  }
  .description {
    position: absolute; top: 848px; width: 100%; text-align: center;
    font-family: "Noto Sans JP", sans-serif; font-weight: 500; font-size: 29px; line-height: 45px;
    color: var(--ink);
  }
</style>
</head>
<body>
<main class="label">
  <div class="label-edge"></div>
  <p class="tagline">WELL-BALANCED SUPERFOOD</p>
  <p class="english-name">Stardust Komorebi Powder</p>

  <svg class="art" width="893" height="1200" viewBox="0 0 893 1200">
    <defs>
      <linearGradient id="banner-red" x1="0" y1="0" x2="0" y2="1">
        <stop offset="0" stop-color="var(--red-hi)"/>
        <stop offset="1" stop-color="var(--red-lo)"/>
      </linearGradient>
      <radialGradient id="glow-gold">
        <stop offset="0" stop-color="var(--sun-soft)"/>
        <stop offset="0.7" stop-color="var(--sun)"/>
        <stop offset="1" stop-color="var(--sun)" stop-opacity="0"/>
      </radialGradient>
      <radialGradient id="glow-soft">
        <stop offset="0" stop-color="#ffe27a" stop-opacity="0.9"/>
        <stop offset="1" stop-color="#ffe27a" stop-opacity="0"/>
      </radialGradient>
      <radialGradient id="powder" cx="0.45" cy="0.4">
        <stop offset="0" stop-color="#e9dcc2"/>
        <stop offset="1" stop-color="#c9b48e"/>
      </radialGradient>
    </defs>

    <!-- stars -->
    <g class="stars" fill="var(--gold-deep)">
      <polygon points="446,166 450,176 461,176 452,182 456,193 446,186 436,193 440,182 431,176 442,176"/>
      <polygon points="178,210 181,218 189,218 183,223 185,231 178,226 171,231 173,223 167,218 175,218"/>
      <polygon points="715,210 718,218 726,218 720,223 722,231 715,226 708,231 710,223 704,218 712,218"/>
    </g>

    <!-- sun glows -->
    <circle cx="220" cy="610" r="110" fill="url(#glow-soft)"/>
    <circle cx="673" cy="610" r="110" fill="url(#glow-soft)"/>
    <circle cx="220" cy="610" r="80" fill="url(#glow-gold)"/>
    <circle cx="673" cy="610" r="80" fill="url(#glow-gold)"/>
    <circle cx="446" cy="690" r="230" fill="url(#glow-soft)"/>

    <!-- banner -->
    <rect x="150" y="205" width="593" height="290" rx="30" fill="var(--gold)" stroke="var(--gold-deep)" stroke-width="4"/>
    <rect x="166" y="221" width="561" height="258" rx="22" fill="url(#banner-red)"/>
    <rect x="176" y="231" width="541" height="238" rx="18" fill="none" stroke="var(--gold)" stroke-width="2"/>

    <!-- product photo area -->
    <circle cx="446" cy="690" r="168" fill="url(#powder)" role="img" aria-label="粉末パウダーの写真"/>
  </svg>

  <h1 class="product-name">星屑の<br>コモレビ<br>パウダー</h1>

  <p class="description">
    食物繊維やビタミン類が豊富な<br>
    スーパーフードのタイガーナッツを<br>
    パウダー状にしました<br>
    手軽に使える料理素材として<br>
    タイガーナッツミルク作りに
  </p>
</main>
</body>
</html>
```